Business Card Design

Hello,
I try and keep my business card fresh and current. So about every year i get a new one. This year I'd like something with a white background and black lettering.
Before you start - I do not want my phone number or any other description on the card other than my url and my email.

I'd like a double sided business card with
TedMarlow.com on one side

and

Ted@TedMarlow.com on the other side of the card

Thinking very minimalistic and modern.
I don't have a particular font i mind or how to capitalize my name or website. This card will lead people to my new website that is being designed to showcase my photography and music.

* Initial thought was the front side of the card having a grid-like pattern built out of dashes or periods, with my website sitting within the pattern and on the back side my email on a stark white background. But that might look completely lame - haha.

I'm looking forward to seeing what you come up with.

thank you,
- ted marlow

Reason: Want to spend some more time with the designs and add a little $. thanks for all the designs - ted

Wanted to add a little $ and spend some more time with the designs.

big thanks to all who have submitted work 

- ted

www.tedmarlow.com
ted@tedmarlow.com

000000
ffffff

• tedmarlow.com
ted@tedmarlow.com
• phone number
any description of what i do, photography or music

```html
<!DOCTYPE html>
<html lang="en">
<head>
<meta charset="utf-8">
<title>Ted Marlow — Business Card</title>
<link href="https://fonts.googleapis.com/css2?family=Lato:wght@300;400;700&display=swap" rel="stylesheet">
<style>
  :root {
    --stage: #d9d9d9;
    --card-white: #ffffff;
    --pattern-light: #f6f6f6;
    --pattern-mid: #ebebeb;
    --ink: #2b2b2b;
    --ink-soft: #3a3a3a;
    --card-black: #1f2020;
    --url-grey: #d6d6d6;
  }
  * { margin: 0; padding: 0; box-sizing: border-box; }
  html, body {
    width: 1200px;
    height: 926px;
    overflow: hidden;
    background: var(--stage);
    font-family: "Lato", "Helvetica Neue", Arial, sans-serif;
  }
  .sheet {
    width: 1200px;
    height: 926px;
    display: flex;
    flex-direction: column;
    align-items: center;
    justify-content: center;
    gap: 42px;
  }
  .card {
    position: relative;
    width: 700px;
    height: 400px;
    overflow: hidden;
    box-shadow: 0 6px 18px rgba(0, 0, 0, 0.18);
  }
  .card--front { background: var(--card-white); }
  .card__pattern {
    position: absolute;
    inset: 0;
    background: radial-gradient(circle at 50% 50%, var(--pattern-light) 0%, var(--pattern-mid) 100%);
  }
  .identity {
    position: absolute;
    left: 196px;
    top: 150px;
    color: var(--ink);
  }
  .identity__name {
    font-size: 44px;
    font-weight: 300;
    letter-spacing: 1px;
    line-height: 1;
  }
  .identity__surname {
    font-weight: 700;
    color: var(--ink-soft);
  }
  .identity__email {
    margin-top: 8px;
    font-size: 27px;
    font-weight: 400;
    line-height: 1;
  }
  .card--back {
    background: var(--card-black);
    display: flex;
    align-items: center;
    justify-content: center;
  }
  .back__url {
    margin-top: -30px;
    color: var(--url-grey);
    font-size: 22px;
    font-weight: 400;
    letter-spacing: 2px;
  }
</style>
</head>
<body>
  <main class="sheet">
    <section class="card card--front">
      <div class="card__pattern" role="img" aria-label="Fine light grey geometric lattice pattern covering the card"></div>
      <div class="identity">
        <h1 class="identity__name">TED <span class="identity__surname">MARLOW</span></h1>
        <p class="identity__email">ted@tedmarlow.com</p>
      </div>
    </section>
    <section class="card card--back">
      <p class="back__url">www.tedmarlow.com</p>
    </section>
  </main>
</body>
</html>
```